Flyer Design for Promoting Arborist Business

Hi guys,
***UPDATE: File pack is available here: https://www.filecrate-example.net/sh/x7k2qq/BBbR4tLmZ9wPdVs?dl=0
We've are a high-end arborist business in Edinburgh and we're now looking to create some promotional flyers to attract new business.
This is an open brief and we're looking for inspiration from our designer.
Our target market for the flyers is people who cannot readily access our online material (e.g. elderly people without internet access), so therefore has to be easily understood.
Trust is a central part of our business and we'd like our photographs on the flyer to build that trust.
The primary method of contact will be telephone, therefore we'd like our phone numbers to be front and centre.
You can see our website here: www.fernhollowtreecare.com
We have a full pack of design material for our logo which can be shared. This includes colours, fonts and logo. It's all as per our website.
Inspire us!
Best,
Malcolm

Look and feel
Each slider illustrates characteristics of the customer's brand and the style your logo design should communicate.

```html
<!DOCTYPE html>
<html lang="en">
<head>
<meta charset="utf-8">
<title>Fern Hollow Tree Care – Flyer</title>
<link href="https://fonts.googleapis.com/css2?family=Cinzel:wght@500;600&family=Source+Sans+3:wght@400;600;700&display=swap" rel="stylesheet">
<style>
  :root{
    --red:#b0161f;
    --ink:#1a1a1a;
    --black:#000;
    --white:#fff;
    --page:#e9e9ea;
  }
  *{box-sizing:border-box;margin:0;padding:0}
  html,body{width:1200px;height:1000px;overflow:hidden;background:var(--page)}
  body{font-family:"Source Sans 3",Arial,sans-serif;color:var(--ink)}
  .flyer{position:absolute;left:250px;top:10px;width:700px;height:980px;background:var(--white);overflow:hidden}
  .brand{position:absolute;left:30px;top:92px;font-family:"Cinzel",serif;font-weight:500;color:var(--ink);line-height:1}
  .brand-mark{display:inline-block;width:18px;height:18px;background:var(--red);margin-bottom:10px}
  .brand-name{font-size:36px;letter-spacing:1px}
  .brand-sub{font-size:21px;letter-spacing:11px;margin-top:8px}
  .swoosh{position:absolute;right:0;top:0;width:410px;height:188px}
  .headline{position:absolute;right:22px;top:38px;text-align:right;font-family:"Cinzel",serif;font-weight:600;color:var(--white);font-size:29px;line-height:31px}
  .photos{position:absolute;left:0;top:198px;width:700px;height:234px;display:flex;gap:5px}
  .photo{flex:1}
  .photo-1{background:linear-gradient(160deg,#7a6a5e,#4a3b32 55%,#8a3b35)}
  .photo-2{background:linear-gradient(150deg,#9fb8cf,#c98a5b 55%,#e8c2b6)}
  .photo-3{background:linear-gradient(170deg,#d9d1c0,#7c6b4d 50%,#5c5a2e)}
  .tab{position:absolute;left:0;background:var(--red);color:var(--white);font-family:"Cinzel",serif;font-weight:500;border-radius:0 18px 18px 0;display:flex;align-items:center;padding-left:25px}
  .tab-qual{top:440px;width:294px;height:33px;font-size:23px}
  .tab-serv{top:686px;width:198px;height:29px;font-size:21px}
  .qual-copy{position:absolute;left:28px;top:483px;width:410px;font-size:10px;line-height:13px;text-align:justify}
  .qual-copy p{margin-bottom:4px}
  .qual-copy .narrow{width:248px}
  .badge{position:absolute;top:590px;height:66px}
  .badge-a{left:290px;width:54px;background:#d7d7d7;border-radius:4px}
  .badge-b{left:360px;width:86px;border:2px solid var(--red);border-radius:6px;background:linear-gradient(var(--white) 70%,var(--red) 70%)}
  .services{position:absolute;top:722px;left:25px;display:grid;grid-template-columns:142px 164px 140px;row-gap:4px;list-style:none;font-size:13.5px}
  .services li{display:flex;align-items:center;height:19px}
  .services li::before{content:"";width:14px;height:7px;background:var(--red);border-radius:14px 2px 14px 2px;margin-right:6px;transform:rotate(-12deg)}
  .notes{position:absolute;left:28px;top:845px;width:440px;font-size:10.5px;line-height:13px;font-weight:600}
  .notes p{margin-bottom:6px}
  .notes .accent{color:var(--red)}
  .service-panel{position:absolute;left:462px;top:432px;width:238px;height:479px;background:var(--black)}
  .icon-card{position:absolute;width:110px;text-align:center;color:var(--white);font-size:14.5px;line-height:16.5px;font-weight:600}
  .icon-disc{width:75px;height:75px;border-radius:50%;background:var(--white);margin:0 auto 17px;display:flex;align-items:center;justify-content:center}
  .icon-disc svg{width:48px;height:48px}
  .phone-bar{position:absolute;left:0;top:911px;width:700px;height:29px;background:var(--red);color:var(--white);text-align:center;font-size:21px;font-weight:700;line-height:29px}
  .site{position:absolute;left:0;top:944px;width:700px;text-align:center;font-size:14px;font-weight:600;letter-spacing:.3px}
</style>
</head>
<body>
<main class="flyer">
  <header>
    <div class="brand">
      <span class="brand-mark"></span>
      <div class="brand-name">FERN HOLLOW</div>
      <div class="brand-sub">TREE CARE</div>
    </div>
    <svg class="swoosh" viewBox="0 0 410 188" aria-hidden="true">
      <path d="M0 92 C70 40 150 4 260 0 L360 0 C390 30 410 70 410 110 L410 188 C330 190 250 180 200 160 C150 140 100 105 0 92 Z" fill="#b0161f"/>
    </svg>
    <h1 class="headline">Professional<br>Edinburgh-Based<br>Tree Surgeons</h1>
  </header>

  <section class="photos">
    <div class="photo photo-1" role="img" aria-label="Climber in safety gear cutting a tree beside a house roof"></div>
    <div class="photo photo-2" role="img" aria-label="Blossom branches in front of a stone castle"></div>
    <div class="photo photo-3" role="img" aria-label="Two arborists in hi-vis gear beside large trees in a park"></div>
  </section>

  <h2 class="tab tab-qual">Our Qualifications</h2>
  <div class="qual-copy">
    <p>We're fully qualified and certified by both Arbor Skills Board and Greenline Awards in aerial and ground-based tree work.</p>
    <p>Our arborist team is trained in the latest arborist techniques and furnished with state-of-the-art equipment to ensure that your tree work is carried out to the highest standard, quickly and with maximum safety.</p>
    <p>We can quickly reduce tree cuttings on site and we provide our disposal services as standard on every job.</p>
    <p class="narrow">We take great pride in our professionalism and the standard of our work and we're fully insured to carry out all our work for your peace of mind.</p>
    <p class="narrow">We offer our emergency call-out service to make trees safe after acute damage, for example due to wind or limb release.</p>
  </div>
  <div class="badge badge-a" role="img" aria-label="Qualification badge"></div>
  <div class="badge badge-b" role="img" aria-label="Training badge"></div>

  <h2 class="tab tab-serv">Our Services</h2>
  <ul class="services">
    <li>Aerial Pruning</li><li>Emergency Response</li><li>Stump Removal</li>
    <li>Aerial Dismantling</li><li>Garden Clearance</li><li>Tree Surveys</li>
    <li>Clear Felling</li><li>Sectional Felling</li><li>Waste Removal</li>
    <li>Crown Lifts</li><li>Site Clearance</li><li>Wood Chipping</li>
    <li>Crown Reductions</li><li>Storm Damage</li>
  </ul>

  <div class="notes">
    <p><span class="accent">We offer a free planning application service</span> to manage the necessary permissions for trees with Tree Protection Orders (TPOs) and in Conservation Areas.</p>
    <p>Unsure if your tree is affected? We can quickly advise. <span class="accent">Contact us</span> with your tree's location for a free confirmation.</p>
  </div>

  <aside class="service-panel">
    <div class="icon-card" style="left:4px;top:25px">
      <div class="icon-disc"><svg viewBox="0 0 48 48" fill="none" stroke="#b0161f" stroke-width="3" stroke-linejoin="round"><path d="M28 6 L40 14 L34 22 L26 16 Z"/><path d="M29 18 L10 40 L14 43 L32 21"/></svg></div>
      Felling and Dismantling
    </div>
    <div class="icon-card" style="left:124px;top:25px">
      <div class="icon-disc"><svg viewBox="0 0 48 48" fill="none" stroke="#b0161f" stroke-width="2.5" stroke-linecap="round"><path d="M24 44 V24 M24 30 L14 18 M24 28 L34 16 M14 18 L8 10 M14 18 L16 8 M34 16 L40 8 M34 16 L30 7 M24 24 V6"/></svg></div>
      Crown Lifts and Reductions
    </div>
    <div class="icon-card" style="left:4px;top:188px">
      <div class="icon-disc"><svg viewBox="0 0 48 48" fill="none" stroke="#b0161f" stroke-width="2.5" stroke-linecap="round"><path d="M4 26 H44 M14 26 L10 18 M24 26 L28 18 M34 26 L30 33 M40 26 L44 20"/></svg></div>
      Aerial Pruning
    </div>
    <div class="icon-card" style="left:124px;top:188px">
      <div class="icon-disc"><svg viewBox="0 0 48 48" fill="none" stroke="#b0161f" stroke-width="3"><rect x="10" y="8" width="28" height="34" rx="2"/><rect x="18" y="5" width="12" height="6" fill="#b0161f"/><path d="M16 20 H32 M16 26 H32 M16 32 H32"/></svg></div>
      Tree Surveys
    </div>
    <div class="icon-card" style="left:4px;top:348px">
      <div class="icon-disc"><svg viewBox="0 0 48 48"><path d="M28 3 L14 26 H23 L18 45 L35 19 H26 Z" fill="#b0161f"/></svg></div>
      Storm Damage
    </div>
    <div class="icon-card" style="left:124px;top:348px">
      <div class="icon-disc"><svg viewBox="0 0 48 48" fill="#b0161f"><ellipse cx="24" cy="14" rx="13" ry="5"/><path d="M11 14 V34 L5 40 H43 L37 34 V14 C37 18 11 18 11 14 Z"/></svg></div>
      Stump Removal
    </div>
  </aside>

  <div class="phone-bar">Emergency? No problem, call us 24/7 on 0131 496 0732</div>
  <div class="site">www.fernhollowtreecare.com</div>
</main>
</body>
</html>
```